Coastal Heritage Dairywrights' Guild needs new business cards

We need new business cards designed and produced. We are likely to need other design work done for ads, flyers etc in future.

We would like to start with an initial business card.

The Coastal Heritage Dairywrights' Guild (CHDG) is a membership-based not-for-profit organisation that looks after the interests of Australia's small to medium artisan cheesemakers, many of whom are also small-scale farmers. The design should be simple, using our logo, but also communicate our artisan cheese and small dairy farm focus.

The first card to be designed and produced is for me, Megan Thorburn. My details are:

Megan Thorburn
Secretary
Coastal Heritage Dairywrights' Guild (CHDG)
http://www.curdandcrockery.org
T +61427583914
E megan.meganthorburn@mailfern.net

I have attached the CHDG logo in jpg form. I have a higher resolution version available if needed.

Thank you!

Megan

Business

Megan Thorburn
Coastal Heritage Dairywrights' Guild
megan.meganthorburn@mailfern.net
+61427583914

Sans Serif

• Logo (see attached file)

```html
<!DOCTYPE html>
<html lang="en">
<head>
<meta charset="utf-8">
<title>CHDG Business Card – Megan Thorburn</title>
<link href="https://fonts.googleapis.com/css2?family=Crimson+Text:wght@400&family=Open+Sans:wght@400;600&display=swap" rel="stylesheet">
<style>
  :root {
    --page-bg: #a9a8ad;
    --card-white: #ffffff;
    --brown: #654525;
    --brown-dark: #5c3f22;
    --cheese: #f2d27a;
    --logo-brown: #6b4a2b;
    --text-light: #ffffff;
  }
  * { margin: 0; padding: 0; box-sizing: border-box; }
  html, body { width: 1200px; height: 1200px; overflow: hidden; }
  body {
    background: var(--page-bg);
    position: relative;
    font-family: "Open Sans", sans-serif;
  }
  .card {
    position: absolute;
    left: 170px;
    width: 860px;
    height: 490px;
    border-radius: 36px;
    overflow: hidden;
    box-shadow: 0 10px 24px rgba(0,0,0,0.22);
  }
  .card--front { top: 80px; background: var(--card-white); }
  .card--back { top: 630px; background: linear-gradient(135deg, var(--brown), var(--brown-dark)); }

  .front-band {
    position: absolute; left: 0; right: 0; bottom: 0; height: 30px;
    background: var(--brown);
  }

  .org-name {
    position: absolute;
    display: flex; align-items: center; gap: 22px;
  }
  .org-name__dot {
    width: 70px; height: 70px; border-radius: 50%;
    background: var(--cheese);
    flex: none;
  }
  .org-name__text {
    font-family: "Crimson Text", serif;
    font-weight: 400;
    color: var(--logo-brown);
    line-height: 1.02;
    letter-spacing: 1px;
  }
  .card--front .org-name { left: 250px; top: 150px; }
  .card--front .org-name__text { font-size: 40px; }

  .back-shapes { position: absolute; inset: 0; }
  .card--back .org-name { left: 90px; top: 160px; }
  .card--back .org-name__dot { width: 56px; height: 56px; }
  .card--back .org-name__text { font-size: 32px; }

  .contact {
    position: absolute; left: 585px; top: 120px; right: 40px;
    color: var(--text-light);
  }
  .contact__name { font-size: 28px; font-weight: 600; line-height: 1.15; white-space: nowrap; }
  .contact__role { font-size: 17px; margin-bottom: 24px; }
  .contact__line {
    display: flex; align-items: center; gap: 11px;
    font-size: 15px; line-height: 1.7; white-space: nowrap;
  }
  .contact__line svg { width: 14px; height: 14px; flex: none; fill: var(--text-light); }
</style>
</head>
<body>

<section class="card card--front" aria-label="Card front">
  <div class="org-name">
    <span class="org-name__dot"></span>
    <div class="org-name__text">Coastal<br>Heritage<br>Dairywrights'<br>Guild</div>
  </div>
  <div class="front-band"></div>
</section>

<section class="card card--back" aria-label="Card back">
  <svg class="back-shapes" viewBox="0 0 860 490" width="860" height="490" aria-hidden="true">
    <circle cx="212" cy="330" r="354" fill="var(--cheese)"/>
    <circle cx="180" cy="320" r="350" fill="var(--card-white)"/>
  </svg>

  <div class="org-name">
    <span class="org-name__dot"></span>
    <div class="org-name__text">Coastal<br>Heritage<br>Dairywrights'<br>Guild</div>
  </div>

  <div class="contact">
    <div class="contact__name">Megan Thorburn</div>
    <div class="contact__role">Secretary</div>
    <div class="contact__line">
      <svg viewBox="0 0 16 16"><path d="M3.5 1.5l2.5 0 1 3.5-1.6 1.2a9 9 0 0 0 4.4 4.4L11 9l3.5 1v2.5c0 1-1 2-2 2C6.5 14.5 1.5 9.5 1.5 3.5c0-1 1-2 2-2z"/></svg>
      <span>+61427583914</span>
    </div>
    <div class="contact__line">
      <svg viewBox="0 0 16 16"><path d="M1 3h14v10H1z M1.8 3.8L8 8.8l6.2-5H1.8z" fill-rule="evenodd"/></svg>
      <span>meganthorburn@mailfern.net</span>
    </div>
    <div class="contact__line">
      <svg viewBox="0 0 16 16"><path d="M8 1a7 7 0 1 0 0 14A7 7 0 0 0 8 1zm0 1.5a5.5 5.5 0 1 1 0 11 5.5 5.5 0 0 1 0-11zM5 6h6v1.2H5zm0 2.8h6V10H5z"/></svg>
      <span>www.curdandcrockery.org</span>
    </div>
  </div>
</section>

</body>
</html>
```